Health Information/Education Logo Design

We need a logo design for a new company based in Atlanta called Meadowlark Health. The program is about patient empowerment. We provide health information and education on how to get healthy, stay healthy, and how to be proactive in your care. We also provide medication and injection training to help patients feel their best and to ensure successful therapy outcomes.
We like the colors yellow, pink, teal and purple and would like to see some or all of these colors in the designs. The final design should communicate caring, considerate, compassionate information, education and training services
Industry/Entity Type
Education
Contact Information for Business Card
Meadowlark Health
Danielle Ostrander RN, MSN, MHA
Nurse Educator
555.214.3096 cell
555.470.2283 fax

```html
<!DOCTYPE html>
<html lang="en">
<head>
<meta charset="utf-8">
<title>Meadowlark Health – Business Card</title>
<link rel="stylesheet" href="https://fonts.googleapis.com/css2?family=Source+Sans+3:wght@400;600&display=swap">
<style>
  :root {
    --backdrop: #000000;
    --card: #ffffff;
    --teal: #1a7d79;
    --blush: #f4c4c5;
    --coral: #f2887a;
  }
  * { margin: 0; padding: 0; box-sizing: border-box; }
  html, body {
    width: 1200px; height: 1000px; overflow: hidden;
    background: var(--backdrop);
  }
  .card {
    position: absolute; left: 275px; top: 311px;
    width: 651px; height: 381px;
    background: var(--card);
    overflow: hidden;
    font-family: "Source Sans 3", "Myriad Pro", sans-serif;
    color: var(--teal);
  }
  .card-stripes { position: absolute; inset: 0; }
  .stripe-light { fill: var(--blush); }
  .stripe-dark { fill: var(--coral); }
  .identity { position: absolute; left: 84px; top: 55px; }
  .identity-name { font-size: 26px; font-weight: 600; line-height: 32px; letter-spacing: 0.2px; }
  .identity-line { font-size: 22px; font-weight: 400; line-height: 36px; }
  .brand {
    position: absolute; left: 325px; top: 205px;
    transform: translate(-50%, -50%);
    display: flex; align-items: center; gap: 8px;
    white-space: nowrap;
  }
  .brand-dot { width: 14px; height: 14px; border-radius: 50%; background: var(--teal); }
  .brand-name { font-size: 19px; font-weight: 600; }
  .contact { position: absolute; left: 380px; top: 266px; font-size: 21px; line-height: 29px; }
  .contact-number { font-weight: 600; }
</style>
</head>
<body>
  <div class="card">
    <svg class="card-stripes" width="651" height="381" viewBox="0 0 651 381" aria-hidden="true">
      <polygon class="stripe-light" points="380,0 651,0 651,271"/>
      <polygon class="stripe-dark" points="560,0 651,0 651,91"/>
      <polygon class="stripe-light" points="0,107 274,381 0,381"/>
      <polygon class="stripe-dark" points="0,287 94,381 0,381"/>
    </svg>

    <div class="identity">
      <p class="identity-name">Danielle Ostrander</p>
      <p class="identity-line">RN, MSN, MHA</p>
      <p class="identity-line">Nurse Educator</p>
    </div>

    <div class="brand">
      <span class="brand-dot"></span>
      <span class="brand-name">Meadowlark Health</span>
    </div>

    <div class="contact">
      <p><span class="contact-number">555.214.3096</span> cell</p>
      <p><span class="contact-number">555.470.2283</span> fax</p>
    </div>
  </div>
</body>
</html>
```